Bellhaven Select Business Card Design Project

About the company: Here at Marigrove Essence, we focus on cosmetic products that based on essential oils and different kinds of plant essences. All of our raw materials are pure organic and specially selected from local producers in Australia.

I'm here to look for a unique business card design, to replace the current one later on, so I don't have many requirements. Why I wanna restrict designers' creativity?

All I know is: 1. do not make it too complicated, straight forward, simple and pure. 2. this design may be used for other purposes (i.e. logo and slogan on the front, Brand Story and contact details at the back). Therefor, I'd like to have the design for 3 layouts, one only have logo, slogan, contact detials, one for the brand story, the other one for the personal business card with staff's mob etc...

A vector graphic is required, i.e. eps, ai, easy for me to resize.

Round Corner.

Thanks
Updates

Plz add "Hand made in Australia" in the design, cheers.

Target Market(s)

Women aged yr 20-50

Industry/Entity Type

Business

Requirements
Must have
• Logo: please see attacment (eps, ai)

Slogan: Dew Touched Delight

Website:www.marigroveessence-demo.com.au

Address: temporary not available

Phone: temporary not available

"Hand made in Australia"

Nice to have
• Prefer round corner

```html
<!DOCTYPE html>
<html lang="en">
<head>
<meta charset="utf-8">
<title>Marigrove Essence – Business Cards</title>
<link rel="stylesheet" href="https://fonts.googleapis.com/css2?family=Ubuntu:wght@400&family=Arimo:wght@400&display=swap">
<style>
  :root {
    --backdrop: #4a4a4a;
    --card: #ffffff;
    --rose-pink: #e24d6e;
    --violet: #9b34c8;
    --logo-pink: #e2607f;
    --name-grey: #555555;
    --info-grey: #4d4d4d;
    --accent-orange: #f08a2c;
    --flower-light: #f6a6bd;
    --flower-deep: #e0567a;
  }
  * { margin: 0; padding: 0; box-sizing: border-box; }
  html, body { width: 1200px; height: 900px; overflow: hidden; }
  body { background: var(--backdrop); position: relative; font-family: "Arimo", Arial, sans-serif; }

  .card {
    position: absolute;
    width: 362px;
    height: 206px;
    background: var(--card);
    border-radius: 14px;
    overflow: hidden;
  }
  .card--front-a { left: 200px; top: 212px; }
  .card--back-a  { left: 668px; top: 212px; height: 208px; }
  .card--front-b { left: 205px; top: 508px; height: 207px; }
  .card--back-b  { left: 673px; top: 508px; }

  .wave { position: absolute; left: 0; bottom: 0; width: 100%; height: 100%; }

  .brand {
    position: absolute;
    font-family: "Ubuntu", sans-serif;
    font-weight: 400;
    color: var(--logo-pink);
    display: flex;
    align-items: center;
    gap: 6px;
    white-space: nowrap;
  }
  .brand__dot { border-radius: 50%; background: var(--logo-pink); flex: none; }
  .slogan {
    position: absolute;
    font-family: "Ubuntu", sans-serif;
    color: var(--violet);
    white-space: nowrap;
  }

  .card--front-a .brand,
  .card--front-b .brand { left: 0; right: 0; justify-content: center; font-size: 24px; }
  .card--front-a .brand__dot,
  .card--front-b .brand__dot { width: 12px; height: 12px; }

  .card--front-a .slogan { left: 192px; top: 38px; font-size: 10px; }
  .card--front-a .brand  { top: 58px; }

  .card--front-b .brand  { top: 30px; }
  .card--front-b .slogan { left: 180px; top: 64px; font-size: 10px; }

  .holder {
    position: absolute;
    font-family: "Ubuntu", sans-serif;
    font-weight: 400;
    font-size: 21px;
    color: var(--name-grey);
    white-space: nowrap;
  }
  .card--back-a .holder { left: 20px; top: 46px; }
  .card--back-b .holder { left: 25px; top: 43px; }

  .card--back-a .brand { right: 16px; top: 22px; font-size: 12px; gap: 4px; }
  .card--back-a .brand__dot { width: 7px; height: 7px; }
  .card--back-b .brand { left: 26px; top: 126px; font-size: 13px; gap: 5px; }
  .card--back-b .brand__dot { width: 8px; height: 8px; }

  .flower {
    position: absolute;
    left: 50px; top: 100px;
    width: 82px; height: 76px;
    border-radius: 50%;
    background: radial-gradient(circle at 50% 45%, var(--flower-light), var(--flower-deep));
  }

  .contact {
    position: absolute;
    padding-left: 7px;
    font-size: 10px;
    line-height: 11.5px;
    font-style: normal;
    color: var(--info-grey);
    white-space: nowrap;
  }
  .card--back-a .contact { left: 170px; top: 114px; border-left: 2px solid var(--accent-orange); padding-top: 12px; padding-bottom: 8px; }
  .card--back-b .contact { left: 170px; top: 113px; border-left: 2px solid var(--violet); padding-top: 11px; padding-bottom: 8px; }

  .strip { position: absolute; left: 0; bottom: 0; width: 100%; height: 17px; }
  .strip svg { position: absolute; inset: 0; width: 100%; height: 100%; }
  .strip__label {
    position: absolute;
    right: 16px; top: 2px;
    font-size: 10px;
    color: #ffffff;
    white-space: nowrap;
  }
</style>
</head>
<body>

  <section class="card card--front-a">
    <p class="slogan">Dew Touched Delight</p>
    <div class="brand"><span class="brand__dot"></span>Marigrove Essence</div>
    <svg class="wave" viewBox="0 0 362 206" preserveAspectRatio="none" aria-hidden="true">
      <path d="M190 152 Q280 134 362 134 L362 206 L190 206 Z" fill="var(--violet)"/>
      <path d="M0 136 Q140 134 230 166 Q300 190 362 206 L0 206 Z" fill="var(--rose-pink)"/>
    </svg>
  </section>

  <section class="card card--back-a">
    <div class="brand"><span class="brand__dot"></span>Marigrove Essence</div>
    <h2 class="holder">Daniel Carver</h2>
    <div class="flower" role="img" aria-label="Pink rose illustration"></div>
    <address class="contact">
      Unit 14, Harbour Lane Plaza<br>
      Riverside North<br>
      Ph: 0400-5550182<br>
      www.marigroveessence-demo.com.au
    </address>
    <div class="strip">
      <svg viewBox="0 0 362 17" preserveAspectRatio="none" aria-hidden="true">
        <polygon points="0,0 217,0 212,17 0,17" fill="var(--rose-pink)"/>
        <polygon points="225,0 362,0 362,17 220,17" fill="var(--violet)"/>
      </svg>
      <span class="strip__label">Hand made in Australia</span>
    </div>
  </section>

  <section class="card card--front-b">
    <div class="brand"><span class="brand__dot"></span>Marigrove Essence</div>
    <p class="slogan">Dew Touched Delight</p>
    <svg class="wave" viewBox="0 0 362 207" preserveAspectRatio="none" aria-hidden="true">
      <path d="M190 157 Q280 136 362 136 L362 207 L190 207 Z" fill="var(--violet)"/>
      <path d="M0 137 Q140 135 230 168 Q300 192 362 207 L0 207 Z" fill="var(--rose-pink)"/>
    </svg>
  </section>

  <section class="card card--back-b">
    <h2 class="holder">Daniel Carver</h2>
    <div class="brand"><span class="brand__dot"></span>Marigrove Essence</div>
    <address class="contact">
      Unit 14, Harbour Lane Plaza<br>
      Riverside North<br>
      Ph: 0400-5550182<br>
      www.marigroveessence-demo.com.au
    </address>
    <div class="strip">
      <svg viewBox="0 0 362 17" preserveAspectRatio="none" aria-hidden="true">
        <polygon points="0,0 217,0 212,17 0,17" fill="var(--rose-pink)"/>
        <polygon points="225,0 362,0 362,17 220,17" fill="var(--violet)"/>
      </svg>
      <span class="strip__label">Hand made in Australia</span>
    </div>
  </section>

</body>
</html>
```